Detox Before & After Charts

I am looking to create a chart/graph to be used to chart a patient's progress before and after using our 15-day detox program. We will be looking for 3 different graphs to be made.
1. A chart showing the before and after symptom scores of 12 patients in a small clinical trial we did. We will use this one to show prospective patients.
2. A chart showing one single patient's "total" symptom scores before and after the detox. We will use this with each patient, before and after they do the detox.
3. A chart showing one patient's before and symptom scores in more detail, showing their scores in each one of the symptom categories. We will do this with each patient, before and after the detox.
For #2 & #3 above, we would want a master template that we could add the scoring for each new patient ourselves.
See attached for rough samples.
Each of these 3 charts should be the same style, but for now, just do chart #3. And after we decide on the designer, then we will have them do the other 2 charts.
And I prefer a line graph over a bar graph for these. I did not mention that at first. Sorry!!

```html
<!DOCTYPE html>
<html lang="en">
<head>
<meta charset="utf-8">
<title>Detox Scores — Before and After</title>
<link rel="stylesheet" href="https://fonts.googleapis.com/css2?family=Caladea:ital,wght@0,400;0,700;1,400&display=swap">
<style>
  :root {
    --ink: #111111;
    --panel-grey: #d0d0d0;
    --before-red: #c0504d;
    --after-green: #9bbb59;
    --paper: #ffffff;
  }
  * { box-sizing: border-box; margin: 0; padding: 0; }
  html, body { width: 1200px; height: 927px; overflow: hidden; background: var(--paper); }
  body { position: relative; font-family: "Caladea", Georgia, serif; color: var(--ink); }

  .patient-info {
    position: absolute; left: 54px; top: 83px; width: 391px; height: 189px;
    border: 2px solid var(--ink); background: var(--panel-grey);
  }
  .patient-info__title {
    height: 50px; background: var(--paper); border-bottom: 3px solid var(--ink);
    display: flex; align-items: center; justify-content: center;
    font-weight: 700; font-size: 17px; letter-spacing: 0.3px;
  }
  .patient-info__field {
    display: flex; align-items: flex-end; margin: 0 0 0 9px;
    font-weight: 700; font-size: 16px; height: 42px; padding-bottom: 1px;
  }
  .patient-info__field:first-of-type { height: 34px; }
  .patient-info__blank { flex: 0 0 auto; border-bottom: 1.5px solid var(--ink); margin-left: 8px; margin-bottom: 4px; }

  .score-table {
    position: absolute; left: 505px; top: 83px; width: 641px; border-collapse: collapse;
    font-weight: 700; font-size: 18px;
  }
  .score-table th, .score-table td { border: 2px solid var(--ink); text-align: center; }
  .score-table thead th { height: 50px; font-size: 17px; }
  .score-table thead th.empty { border: none; border-bottom: 3px solid var(--ink); }
  .score-table .col-before { width: 116px; background: var(--before-red); color: #fff; }
  .score-table .col-after { width: 112px; background: var(--after-green); color: #fff; }
  .score-table .col-change { width: 117px; }
  .score-table .row-label { text-align: right; padding-right: 8px; font-size: 17px; }
  .score-table .row-symptoms td { height: 67px; background: var(--panel-grey); }
  .score-table .row-weight td { height: 72px; }

  .chart-title {
    position: absolute; left: 0; width: 1200px; top: 302px; text-align: center;
    font-weight: 700; font-size: 27px;
  }
  .chart { position: absolute; left: 0; top: 0; }
  .chart text { font-family: "Caladea", Georgia, serif; fill: var(--ink); }
  .axis-label { font-style: italic; font-size: 14px; }
  .axis-title { font-weight: 700; font-size: 20px; }
  .cell-text { font-size: 14px; }
</style>
</head>
<body>

<section class="patient-info">
  <div class="patient-info__title">PATIENT INFORMATION</div>
  <div class="patient-info__field">NAME: <span class="patient-info__blank" style="width:256px"></span></div>
  <div class="patient-info__field">BEFORE DATE: <span class="patient-info__blank" style="width:196px"></span></div>
  <div class="patient-info__field">AFTER DATE: <span class="patient-info__blank" style="width:206px"></span></div>
</section>

<table class="score-table">
  <thead>
    <tr>
      <th class="empty"></th>
      <th class="col-before">BEFORE</th>
      <th class="col-after">AFTER</th>
      <th class="col-change">CHANGE</th>
    </tr>
  </thead>
  <tbody>
    <tr class="row-symptoms"><td class="row-label">TOTAL SYMPTOM SCORES</td><td>75</td><td>25</td><td>-66%</td></tr>
    <tr class="row-weight"><td class="row-label">WEIGHT</td><td>140</td><td>131</td><td>-9</td></tr>
  </tbody>
</table>

<h1 class="chart-title">DETOX SCORES — Before and After</h1>

<svg class="chart" width="1200" height="927" viewBox="0 0 1200 927">
  <defs>
    <linearGradient id="before-fill" x1="0" y1="0" x2="0" y2="1">
      <stop offset="0" stop-color="#cd5350"/><stop offset="1" stop-color="#752224"/>
    </linearGradient>
    <linearGradient id="after-fill" x1="0" y1="0" x2="0" y2="1">
      <stop offset="0" stop-color="#a2c35f"/><stop offset="1" stop-color="#5c7b2a"/>
    </linearGradient>
  </defs>

  <!-- horizontal grid -->
  <g stroke="#111" stroke-width="1">
    <line x1="158" y1="358" x2="1129" y2="358"/><line x1="158" y1="399" x2="1129" y2="399"/>
    <line x1="158" y1="440" x2="1129" y2="440"/><line x1="158" y1="481" x2="1129" y2="481"/>
    <line x1="158" y1="522" x2="1129" y2="522"/><line x1="158" y1="563" x2="1129" y2="563"/>
    <line x1="158" y1="604" x2="1129" y2="604"/><line x1="158" y1="645" x2="1129" y2="645"/>
    <line x1="158" y1="686" x2="1129" y2="686"/><line x1="158" y1="727" x2="1129" y2="727"/>
    <line x1="158" y1="768" x2="1129" y2="768"/>
    <line x1="95" y1="790" x2="1129" y2="790"/>
    <line x1="95" y1="814" x2="1129" y2="814"/>
    <line x1="95" y1="836" x2="1129" y2="836"/>
    <line x1="95" y1="790" x2="95" y2="836"/>
  </g>
  <!-- minor ticks -->
  <line x1="156" y1="358" x2="156" y2="768" stroke="#111" stroke-width="6" stroke-dasharray="1 7.2"/>

  <!-- vertical column rules -->
  <g stroke="#111" stroke-width="1">
    <line x1="158" y1="358" x2="158" y2="836"/><line x1="227.4" y1="358" x2="227.4" y2="836"/>
    <line x1="296.7" y1="358" x2="296.7" y2="836"/><line x1="366.1" y1="358" x2="366.1" y2="836"/>
    <line x1="435.4" y1="358" x2="435.4" y2="836"/><line x1="504.8" y1="358" x2="504.8" y2="836"/>
    <line x1="574.2" y1="358" x2="574.2" y2="836"/><line x1="643.5" y1="358" x2="643.5" y2="836"/>
    <line x1="712.9" y1="358" x2="712.9" y2="836"/><line x1="782.2" y1="358" x2="782.2" y2="836"/>
    <line x1="851.6" y1="358" x2="851.6" y2="836"/><line x1="921" y1="358" x2="921" y2="836"/>
    <line x1="990.3" y1="358" x2="990.3" y2="836"/><line x1="1059.7" y1="358" x2="1059.7" y2="836"/>
    <line x1="1129" y1="358" x2="1129" y2="836"/>
  </g>

  <!-- before bars -->
  <g fill="url(#before-fill)">
    <rect x="173" y="718.8" width="20" height="49.2"/>
    <rect x="242.4" y="640.9" width="20" height="127.1"/>
    <rect x="311.7" y="665.5" width="20" height="102.5"/>
    <rect x="381.1" y="718.8" width="20" height="49.2"/>
    <rect x="450.4" y="718.8" width="20" height="49.2"/>
    <rect x="519.8" y="718.8" width="20" height="49.2"/>
    <rect x="589.2" y="616.3" width="20" height="151.7"/>
    <rect x="658.5" y="718.8" width="20" height="49.2"/>
    <rect x="727.9" y="686" width="20" height="82"/>
    <rect x="797.2" y="583.5" width="20" height="184.5"/>
    <rect x="866.6" y="358" width="20" height="410"/>
    <rect x="936" y="645" width="20" height="123"/>
    <rect x="1005.3" y="665.5" width="20" height="102.5"/>
    <rect x="1074.7" y="751.6" width="20" height="16.4"/>
  </g>
  <!-- after bars -->
  <g fill="url(#after-fill)">
    <rect x="193" y="718.8" width="20" height="49.2"/>
    <rect x="539.8" y="743.4" width="20" height="24.6"/>
    <rect x="747.9" y="747.5" width="20" height="20.5"/>
    <rect x="817.2" y="727" width="20" height="41"/>
    <rect x="886.6" y="706.5" width="20" height="61.5"/>
    <rect x="956" y="747.5" width="20" height="20.5"/>
  </g>

  <!-- y-axis labels -->
  <g class="axis-label" text-anchor="end">
    <text x="142" y="363">100%</text><text x="142" y="404">90%</text>
    <text x="142" y="445">80%</text><text x="142" y="486">70%</text>
    <text x="142" y="527">60%</text><text x="142" y="568">50%</text>
    <text x="142" y="609">40%</text><text x="142" y="650">30%</text>
    <text x="142" y="691">20%</text><text x="142" y="732">10%</text>
    <text x="142" y="773">0%</text>
  </g>
  <text class="axis-title" transform="translate(94 563) rotate(-90)" text-anchor="middle">SYMPTOM SCORE — Percentage</text>

  <!-- data table -->
  <rect x="101" y="797" width="7" height="7" fill="var(--before-red)"/>
  <rect x="101" y="821" width="7" height="7" fill="var(--after-green)"/>
  <g class="cell-text">
    <text x="112" y="807">Before</text>
    <text x="112" y="831">After</text>
  </g>
  <g class="cell-text" text-anchor="middle">
    <text x="192.7" y="784">Digestion</text><text x="262" y="784">Emotions</text>
    <text x="331.4" y="784">Eyes</text><text x="400.8" y="784">Lungs</text>
    <text x="470.1" y="784">Mind</text><text x="539.5" y="784">Energy</text>
    <text x="608.9" y="784">Head</text><text x="678.2" y="784">Ears</text>
    <text x="747.6" y="784">Mouth</text><text x="816.9" y="784">Skin</text>
    <text x="886.3" y="784">Pain</text><text x="955.7" y="784">Nose</text>
    <text x="1025" y="784">Heart</text><text x="1094.4" y="784">Weight</text>

    <text x="192.7" y="807">12%</text><text x="262" y="807">31%</text>
    <text x="331.4" y="807">25%</text><text x="400.8" y="807">12%</text>
    <text x="470.1" y="807">12%</text><text x="539.5" y="807">12%</text>
    <text x="608.9" y="807">37%</text><text x="678.2" y="807">12%</text>
    <text x="747.6" y="807">20%</text><text x="816.9" y="807">45%</text>
    <text x="886.3" y="807">100%</text><text x="955.7" y="807">30%</text>
    <text x="1025" y="807">25%</text><text x="1094.4" y="807">4%</text>

    <text x="192.7" y="831">12%</text><text x="262" y="831">0%</text>
    <text x="331.4" y="831">0%</text><text x="400.8" y="831">0%</text>
    <text x="470.1" y="831">0%</text><text x="539.5" y="831">6%</text>
    <text x="608.9" y="831">0%</text><text x="678.2" y="831">0%</text>
    <text x="747.6" y="831">5%</text><text x="816.9" y="831">10%</text>
    <text x="886.3" y="831">15%</text><text x="955.7" y="831">5%</text>
    <text x="1025" y="831">0%</text><text x="1094.4" y="831">0%</text>
  </g>
</svg>

</body>
</html>
```